Business Card Design for Photographer

Updating business card design. Must use included logo. We're a luxury wedding photography business. Elegancy, luxury, consistency are messages we wish to convey.

Visit our website at www.colvanderose.com to familiarize yourself more with our brand design currently (fonts, colors etc.). This is what we want to maintain.

Target Market(s)

Luxury Brides and Grooms

Industry/Entity Type

Wedding

Contact Information for Business Card

Current logo (attached to brief)
Name: Colin Vanderose
Phone: 5871302948
website/blog
Email

Requirements
Must have
• Current logo (attached to brief)
• Name: Colin Vanderose
• Phone: 5871302948
• website/blog
• Email
• @colvanderose username
Should not have
• bright colors, fonts that don't suit our brand (visit www.colvanderose.com)

```html
<!DOCTYPE html>
<html lang="en">
<head>
<meta charset="utf-8">
<title>Colin Vanderose Photographers – Business Card</title>
<link rel="stylesheet" href="https://fonts.googleapis.com/css2?family=Lato:wght@400;700&family=Pinyon+Script&display=swap">
<style>
  :root {
    --page: #ffffff;
    --card-edge: #e3e4e4;
    --card-light: #fbfbfb;
    --ink-grey: #6f6f6f;
    --band: #767676;
    --band-text: #ffffff;
    --script-ink: #1e1e1e;
    --mark-tone: #dcdddd;
  }
  * { margin: 0; padding: 0; box-sizing: border-box; }
  html, body {
    width: 953px; height: 1200px; overflow: hidden;
    background: var(--page);
  }
  .sheet { position: relative; width: 953px; height: 1200px; }
  .card {
    position: absolute; left: 112px; width: 704px; height: 424px;
    background: radial-gradient(ellipse 70% 85% at 68% 45%, var(--card-light) 0%, #f1f2f2 45%, var(--card-edge) 100%);
    box-shadow: 0 0 14px rgba(0,0,0,0.18);
    overflow: hidden;
  }
  .card--front { top: 125px; }
  .card--back { top: 612px; }
  .card__ornament {
    position: absolute; left: 0; top: 0; width: 330px; height: 370px;
    background: radial-gradient(ellipse 60% 70% at 45% 50%, var(--mark-tone) 0%, rgba(220,221,221,0) 100%);
    opacity: 0.7;
  }
  .card__band {
    position: absolute; left: 0; bottom: 0; width: 100%; height: 49px;
    background: var(--band);
    display: flex; align-items: center; justify-content: center;
  }
  .card__url {
    font-family: "Lato", sans-serif; font-weight: 700;
    font-size: 19px; letter-spacing: 0.16em;
    color: var(--band-text); text-transform: uppercase;
  }
  .brand {
    position: absolute; left: 0; width: 100%; top: 93px;
    text-align: center; color: var(--ink-grey);
    font-family: "Lato", sans-serif;
  }
  .brand__square {
    display: block; width: 84px; height: 84px; margin: 0 auto;
    background: var(--band);
  }
  .brand__name {
    margin-top: 40px;
    font-size: 33px; font-weight: 400; letter-spacing: 0.16em;
    text-transform: uppercase; line-height: 1;
  }
  .brand__trade {
    margin-top: 22px;
    font-size: 18px; font-weight: 400; letter-spacing: 0.42em;
    text-transform: uppercase; line-height: 1;
  }
  .contact {
    position: absolute; right: 49px; top: 80px;
    text-align: right; font-family: "Pinyon Script", cursive;
    color: var(--script-ink); list-style: none;
  }
  .contact__name { font-size: 32px; line-height: 50px; }
  .contact__line { font-size: 27px; line-height: 50px; }
  .contact__social { font-size: 24px; line-height: 44px; color: var(--ink-grey); }
</style>
</head>
<body>
<main class="sheet">
  <section class="card card--front">
    <div class="card__ornament" role="img" aria-label="Faint large monogram decoration"></div>
    <div class="brand">
      <span class="brand__square" aria-hidden="true"></span>
      <p class="brand__name">Colin Vanderose</p>
      <p class="brand__trade">Photographers</p>
    </div>
    <div class="card__band"><span class="card__url">www.colvanderose.com</span></div>
  </section>

  <section class="card card--back">
    <div class="card__ornament" role="img" aria-label="Faint large monogram decoration"></div>
    <ul class="contact">
      <li class="contact__name">Colin Vanderose</li>
      <li class="contact__line">(587) 130-2948</li>
      <li class="contact__line">colin@colvanderose.com</li>
      <li class="contact__social">@colvanderose</li>
    </ul>
    <div class="card__band"><span class="card__url">www.colvanderose.com</span></div>
  </section>
</main>
</body>
</html>
```